PerkParcel.com.au Web Redesign

We need a web redesign for our existing website at http://perkparcel.com.au. Our website hosts a registration form for users who are interested in surveys, samples/trials, competitions (contests), and freebie offers. We rely heavily on emails as our main tool to communicate with our users. The current theme of our website is really white and bright. We would like to see a rather bold but playful theme like red, orange, and dark grey. The final design should be able to: 1) entice users to register; 2) look fun & playful; 3) have the modern, but colorful touch; and 4) present the theme of the offers (i.e. Brims, Lark/Plumfields, and Marlow Finch gift cards). The current logo can be redesigned into a new logo to suit the new web design.
Updates

Your new design must cover the following pages:

/index.html
/catalogue.html
/confirm-your-subscription.html
/contact-us.html
/daily-deals.html
/faqs.html
/terms-of-use.html
/thank-you.html

I missed out two extra pages that should be included in this project

/restaurant.html
/travel.html

Project Deadline Extended
Reason: Deadline is now extended by 15 more days. This should give you more time to be creative.

Target Market(s)

Age 18-65, both males & females, any occupations.

Requirements
Must have
• The new design must have the corresponding theme of the offer presented (Brims, LARK/Plumfields, and Marlow Finch).
Nice to have
• The current layout of our website crams all 3 gift card offers into one page. Feel free to redesign the website into 3 different pages with each page containing a dedicated offer. This will enhance the theme of the offer presented.

```html
<!DOCTYPE html>
<html lang="en">
<head>
<meta charset="utf-8">
<title>Perk Parcel</title>
<link href="https://fonts.googleapis.com/css2?family=Roboto+Condensed:wght@400;700&family=Roboto:wght@400&display=swap" rel="stylesheet">
<style>
:root{
  --red:#e33b3b;
  --orange:#ff9a00;
  --flame:#ff5a14;
  --slate:#47505a;
  --slate-mid:#5c6773;
  --slate-light:#6e7a87;
  --white:#ffffff;
  --ink:#555c63;
  --muted:#b5bcc4;
}
*{box-sizing:border-box;margin:0;padding:0}
html,body{width:1022px;height:1200px;overflow:hidden;background:var(--slate)}
body{font-family:"Roboto",Arial,sans-serif}
.page{position:absolute;left:0;top:0;width:1200px;height:1409px;transform:scale(0.85167);transform-origin:0 0;background:var(--slate)}
.cond{font-family:"Roboto Condensed","Arial Narrow",sans-serif}
.abs{position:absolute}

.hero{position:absolute;left:0;top:0;width:1200px;height:655px;
  background:radial-gradient(ellipse 520px 420px at 640px 300px,#ffc400 0%,#ff8a00 35%,#ff5a14 62%,var(--red) 100%)}
.header{position:absolute;left:120px;top:32px;width:960px;height:56px;background:var(--white)}
.header-base{position:absolute;left:120px;top:88px;width:960px;height:12px;background:linear-gradient(#e4e4e4,#cfcfcf);clip-path:polygon(0 0,100% 0,97% 100%,3% 100%)}
.header-shadow{position:absolute;left:150px;top:100px;width:906px;height:4px;background:rgba(150,30,20,.5);border-radius:50%}
.logo{position:absolute;left:130px;top:36px;font-family:"Roboto Condensed",sans-serif;font-weight:700;font-size:30px;color:var(--red);letter-spacing:-.5px}
.tagline{position:absolute;left:130px;top:70px;font-size:10px;color:#666;letter-spacing:.3px}
.nav{position:absolute;top:52px;left:392px;display:flex;gap:0;font-family:"Roboto Condensed",sans-serif;font-size:14px;color:var(--ink)}
.nav span{position:absolute;white-space:nowrap}

.photo{position:absolute;left:110px;top:160px;width:570px;height:465px;
  background:radial-gradient(ellipse at 50% 55%,rgba(255,235,200,.55),rgba(255,140,60,.15) 60%,rgba(255,90,20,0) 75%)}
.dots{position:absolute;left:131px;top:631px;display:flex;gap:5px}
.dots i{width:5px;height:5px;border-radius:50%;background:#c53a2a;display:block}

.register{position:absolute;left:687px;top:145px;width:393px;height:462px;background:linear-gradient(#ffa300,#ff9200)}
.register h2{position:absolute;left:0;width:100%;top:16px;text-align:center;font-family:"Roboto Condensed",sans-serif;font-weight:400;font-size:36px;color:var(--white)}
.register .sub{position:absolute;left:0;width:100%;top:52px;text-align:center;font-family:"Roboto Condensed",sans-serif;font-size:14px;color:var(--white)}
.field{position:absolute;left:18px;width:353px;height:28px}
.field label{position:absolute;left:0;top:6px;font-family:"Roboto Condensed",sans-serif;font-size:13px;color:var(--white)}
.field .box{position:absolute;left:113px;top:0;width:240px;height:28px;background:var(--white);border-radius:1px}
.consent{position:absolute;left:131px;top:384px;width:240px}
.consent .tick{position:absolute;left:0;top:5px;width:15px;height:15px;background:var(--white)}
.consent p{position:absolute;left:22px;top:1px;font-size:9px;line-height:12px;color:var(--white)}
.submit{position:absolute;left:132px;top:419px;width:83px;height:35px;border:1px solid #e07a00;background:linear-gradient(#ffb300,#ff9c00);color:var(--white);font-family:"Roboto Condensed",sans-serif;font-size:18px;text-align:center;line-height:33px}

.banner{position:absolute;left:120px;top:672px;width:960px;height:160px;background:var(--slate-mid);text-align:center;color:var(--white)}
.banner h1{margin-top:10px;font-family:"Roboto Condensed",sans-serif;font-weight:400;font-size:30px;color:var(--flame)}
.banner p{margin:12px auto 0;width:940px;font-family:"Roboto Condensed",sans-serif;font-size:18px;line-height:22px}

.card{position:absolute;top:851px;width:300px;height:140px;color:var(--white);overflow:hidden}
.card h3{position:absolute;left:16px;top:8px;font-family:"Roboto Condensed",sans-serif;font-weight:400;font-size:32px}
.card ul{position:absolute;left:18px;top:56px;list-style:none;font-size:14px;line-height:24px}
.card li{padding-left:22px;position:relative}
.card li:before{content:"";position:absolute;left:2px;top:8px;width:8px;height:8px;border-radius:50%;background:rgba(0,0,0,.22)}
.tag{position:absolute;right:0;top:70px;width:80px;height:70px;background:var(--white);clip-path:polygon(0 0,100% 14%,100% 100%,0 100%);text-align:center;font-family:"Roboto Condensed",sans-serif;color:var(--red)}
.tag b{display:block;margin-top:10px;font-weight:400;font-size:30px}
.tag span{display:block;font-size:16px;margin-top:-2px}
.brims{left:120px;background:var(--red)}
.lark{left:451px;background:var(--orange)}
.marlow{left:781px;background:var(--slate-light)}

.lead{position:absolute;left:120px;top:1027px;font-family:"Roboto Condensed",sans-serif;font-size:20px;color:var(--white)}
.col{position:absolute;top:1072px;width:311px}
.col h4{font-family:"Roboto Condensed",sans-serif;font-weight:400;font-size:20px;color:var(--orange)}
.col p{margin-top:9px;font-size:14px;line-height:18px;color:var(--white);text-align:justify}
.more{display:inline-block;margin-top:7px;background:var(--red);color:var(--white);font-family:"Roboto Condensed",sans-serif;font-size:14px;padding:6px 12px}

.why{position:absolute;left:788px;top:1028px;width:282px}
.why h4{padding-left:7px;font-family:"Roboto Condensed",sans-serif;font-weight:400;font-size:24px;color:var(--white);height:34px}
.why li{list-style:none;height:29px;border-bottom:1px solid var(--slate);background:var(--slate-light);color:var(--white);font-family:"Roboto Condensed",sans-serif;font-size:14px;line-height:28px;padding-left:43px;position:relative}
.why li svg{position:absolute;left:12px;top:7px}

.rule{position:absolute;left:120px;top:1310px;width:960px;height:1px;background:#6a737d}
.foot-links{position:absolute;left:118px;top:1334px;font-size:14px;color:var(--muted);line-height:18px}
.social{position:absolute;left:954px;top:1339px;display:flex;gap:4px}
.social i{display:block;width:26px;height:26px;border-radius:50%;background:var(--white)}
</style>
</head>
<body>
<div class="page">
  <section class="hero">
    <div class="header"></div>
    <div class="header-base"></div>
    <div class="header-shadow"></div>
    <div class="logo">Perk Parcel</div>
    <div class="tagline">BRINGING AUSSIE'S BEST REWARDS TO YOU</div>
    <nav class="nav" aria-label="Main">
      <span style="left:0">HOME</span>
      <span style="left:85px">COMPETITIONS</span>
      <span style="left:213px">SURVEYS</span>
      <span style="left:309px">FREEBIES</span>
      <span style="left:407px">FAQS</span>
      <span style="left:481px">ABOUT US</span>
      <span style="left:583px">TERMS OF USE</span>
    </nav>

    <div class="photo" role="img" aria-label="Photo of a young woman with headphones lying down using a laptop"></div>
    <div class="dots"><i></i><i></i><i></i></div>

    <form class="register">
      <h2>Register Here!</h2>
      <div class="sub">Subscribe now for your chance to win our monthly rewards!</div>
      <div class="field" style="top:86px"><label>First Name:</label><div class="box"></div></div>
      <div class="field" style="top:119px"><label>Last Name:</label><div class="box"></div></div>
      <div class="field" style="top:152px"><label>E-mail:</label><div class="box"></div></div>
      <div class="field" style="top:185px"><label>Gender:</label><div class="box"></div></div>
      <div class="field" style="top:218px"><label>Year of Birth:</label><div class="box"></div></div>
      <div class="field" style="top:251px"><label>Suburb:</label><div class="box"></div></div>
      <div class="field" style="top:284px"><label>Post Code:</label><div class="box"></div></div>
      <div class="field" style="top:317px"><label>State:</label><div class="box"></div></div>
      <div class="field" style="top:350px"><label>Select Your Prize:</label><div class="box"></div></div>
      <div class="consent"><div class="tick"></div><p>By ticking this box, you agree to subscribe to our newsletter and accept our Terms of Use.</p></div>
      <div class="submit">SUBMIT</div>
    </form>
  </section>

  <section class="banner">
    <h1>WIN A $500 GIFT CARD OF YOUR CHOICE EVERY MONTH!</h1>
    <p>Love shopping but hate the dent in your pocketbook afterwards?<br>Sign up for FREE with Perk Parcel and enter into our monthly shopping spree sweepstakes for your chance to win $500 gift certificates of your choice. Plus, members will also have access to our exclusive competitions, paid surveys, and freebies. With Perk Parcel, the rewarding experience will never end.</p>
  </section>

  <article class="card brims">
    <h3>BRIMS &amp; TALLOW</h3>
    <ul><li>Lots Of Stores</li><li>Millions OF Gifts</li><li>Maximum Choice</li></ul>
    <div class="tag"><b>$599</b><span>Gift Card</span></div>
  </article>
  <article class="card lark">
    <h3>LARK</h3>
    <ul><li>Perfect Gift</li><li>Buy Anything</li><li>Choice of Store</li></ul>
    <div class="tag"><b>$599</b><span>Gift Card</span></div>
  </article>
  <article class="card marlow">
    <h3>MARLOW FINCH</h3>
    <ul><li>World of choice</li><li>Finest Brands</li><li>Wonderful Gifts</li></ul>
    <div class="tag"><b>$599</b><span>Gift Card</span></div>
  </article>

  <h2 class="lead">Australia's Leading Source of Online Competitions &amp; Surveys Rewarding Offers Only</h2>
  <div class="col" style="left:119px">
    <h4>Rewarding Offers Only</h4>
    <p>At Perk Parcel, we bring you the most popular competitions, surveys, freebies, and various samples and trials so that you can maximize your chance to be rewarded. Simply sign up with us and enter the chance to win our monthly $500 gift cards of your choice. This is just the beginning of the most rewarding experience...</p>
    <span class="more">MORE</span>
  </div>
  <div class="col" style="left:450px">
    <h4>It is always FREE!</h4>
    <p>By signing up, you will receive our weekly exclusive offers which are available to our members only. Registration is 100% free! You pay no fees, no subscriptions, no credit cards, and no hassles from telemarketers. We present you with the offers in your e-mail, you simply choose the ones that interest you.</p>
    <span class="more">MORE</span>
  </div>

  <aside class="why">
    <h4>Why Subscribe?</h4>
    <ul>
      <li><svg width="14" height="14" viewBox="0 0 14 14"><circle cx="7" cy="7" r="7" fill="#4a535d"/><path d="M5.5 4l3 3-3 3" stroke="#9aa3ad" stroke-width="1.6" fill="none"/></svg>Free Registration</li>
      <li><svg width="14" height="14" viewBox="0 0 14 14"><circle cx="7" cy="7" r="7" fill="#4a535d"/><path d="M5.5 4l3 3-3 3" stroke="#9aa3ad" stroke-width="1.6" fill="none"/></svg>Greater Chance to Win</li>
      <li><svg width="14" height="14" viewBox="0 0 14 14"><circle cx="7" cy="7" r="7" fill="#4a535d"/><path d="M5.5 4l3 3-3 3" stroke="#9aa3ad" stroke-width="1.6" fill="none"/></svg>Privacy Protection</li>
      <li><svg width="14" height="14" viewBox="0 0 14 14"><circle cx="7" cy="7" r="7" fill="#4a535d"/><path d="M5.5 4l3 3-3 3" stroke="#9aa3ad" stroke-width="1.6" fill="none"/></svg>Monthly Winning Draw</li>
      <li><svg width="14" height="14" viewBox="0 0 14 14"><circle cx="7" cy="7" r="7" fill="#4a535d"/><path d="M5.5 4l3 3-3 3" stroke="#9aa3ad" stroke-width="1.6" fill="none"/></svg>No Credit Card Required</li>
      <li><svg width="14" height="14" viewBox="0 0 14 14"><circle cx="7" cy="7" r="7" fill="#4a535d"/><path d="M5.5 4l3 3-3 3" stroke="#9aa3ad" stroke-width="1.6" fill="none"/></svg>Exclusive Online Offers</li>
      <li><svg width="14" height="14" viewBox="0 0 14 14"><circle cx="7" cy="7" r="7" fill="#4a535d"/><path d="M5.5 4l3 3-3 3" stroke="#9aa3ad" stroke-width="1.6" fill="none"/></svg>Easy to Unsubscribe</li>
    </ul>
  </aside>

  <div class="rule"></div>
  <footer class="foot-links">Privacy Policy &nbsp;|&nbsp; FAQs &nbsp;|&nbsp; About Us &nbsp;|&nbsp; Contact Us &nbsp;|&nbsp; Terms of Use<br>Perk Parcel © 2013</footer>
  <div class="social" aria-label="Social links"><i></i><i></i><i></i><i></i></div>
</div>
</body>
</html>
```